Full Page Marlow 50 Ad

We need a full page magazine ad. Our company is a site construction company - meaning we build lakes, ponds, do brush clearing for farmers and ranchers. For commercial customers, we build building pads, site clearing, pavement and soil stabilization. The final design should show what we do. Our website is www.dunrockgraders.com

```html
<!DOCTYPE html>
<html lang="en">
<head>
<meta charset="utf-8">
<title>Dunrock Grading Co. – Full Page Ad</title>
<link rel="stylesheet" href="https://fonts.googleapis.com/css2?family=Bebas+Neue&family=Poppins:wght@500;600&display=swap">
<style>
  :root{
    --yellow:#f3b52b;
    --ink:#111111;
    --charcoal:#2b2b2b;
    --paper:#ffffff;
    --strip:#e6e6e8;
    --sky:#6e9fd6;
    --sand:#cfc3a6;
    --steel:#6d6d6d;
  }
  *{box-sizing:border-box;margin:0;padding:0}
  html,body{width:727px;height:1200px;overflow:hidden;background:var(--paper)}
  .ad{position:relative;width:727px;height:1200px;overflow:hidden;font-family:"Poppins",sans-serif;color:var(--ink)}
  .hero-photo{position:absolute;left:0;top:0;width:727px;height:700px;
    background:linear-gradient(160deg,var(--sky) 0%,#a9c3e0 22%,#d6a92c 40%,#b88d25 55%,var(--sand) 72%,var(--steel) 100%)}
  .panels{position:absolute;left:0;top:0}

  .brand{position:absolute;right:40px;top:78px;display:flex;align-items:center;gap:10px}
  .brand-mark{width:22px;height:22px;background:var(--ink)}
  .brand-name{font-family:"Bebas Neue",sans-serif;font-size:66px;line-height:1;color:var(--ink);padding-top:6px}

  .intro{position:absolute;left:0;top:225px;width:330px;height:374px;background:rgba(30,30,30,.86);border-radius:0 22px 22px 0;color:var(--paper)}
  .intro-head{position:absolute;left:56px;top:26px;font-family:"Bebas Neue",sans-serif;font-weight:400;text-transform:uppercase;white-space:nowrap}
  .intro-head span{display:block;line-height:1}
  .intro-head .small{font-size:46px}
  .intro-head .big{font-size:88px;color:var(--yellow);margin:4px 0 8px;line-height:.95}
  .intro-head .small + .small{margin-top:4px}
  .intro-body{position:absolute;left:56px;top:288px;width:260px;font-size:15px;font-weight:500;line-height:20px;white-space:nowrap}

  .photo{position:absolute;border:6px solid var(--paper);box-shadow:0 4px 10px rgba(0,0,0,.3)}
  .photo-lake-dig{left:38px;top:640px;width:226px;height:216px;transform:rotate(-5deg);background:linear-gradient(180deg,#7fb0e6 0%,#cfe0ef 35%,#5f6b3e 45%,#6e5a42 100%)}
  .photo-aerial{left:250px;top:632px;width:228px;height:214px;transform:rotate(5deg);background:linear-gradient(135deg,#7d93a3,#5a7560 60%,#9ab0b8)}
  .photo-pond{left:480px;top:636px;width:218px;height:204px;transform:rotate(2deg);background:linear-gradient(180deg,#a8c1de 0%,#6f8ea8 38%,#7da94a 60%,#4f7a33 82%,#8b6c33 100%)}

  .services-farm{position:absolute;left:28px;top:898px;width:320px;font-size:20px;font-weight:500;line-height:33px;text-align:center;white-space:nowrap}
  .commercial{position:absolute;left:396px;top:877px;width:290px;text-align:center}
  .commercial-tag{display:inline-block;background:var(--ink);color:var(--paper);font-size:13px;font-weight:600;padding:6px 14px;border-radius:4px;line-height:1.2}
  .commercial-tag em{font-style:normal;color:var(--yellow)}
  .commercial-text{margin-top:8px;font-size:20px;font-weight:500;line-height:30px;white-space:nowrap}

  .cert-strip{position:absolute;left:0;top:1040px;width:727px;height:66px;background:var(--strip);display:flex;align-items:center;justify-content:center;font-size:18px;font-weight:500}
  .contact-bar{position:absolute;left:0;top:1106px;width:727px;height:94px}
  .contact{position:absolute;top:0;height:94px;display:flex;align-items:center;gap:10px;font-family:"Bebas Neue",sans-serif;line-height:1;white-space:nowrap}
  .contact span{padding-top:5px}
  .contact-web{left:42px;color:var(--paper);font-size:38px}
  .contact-phone{left:428px;color:var(--ink);font-size:46px}
  .contact svg{flex:none}
</style>
</head>
<body>
<main class="ad">
  <div class="hero-photo" role="img" aria-label="Photo of a large yellow earthmoving scraper with a big tyre on a dirt site under a blue sky"></div>

  <svg class="panels" width="727" height="1200" viewBox="0 0 727 1200" aria-hidden="true">
    <polygon points="0,668 727,555 727,1040 0,1040" fill="var(--paper)"/>
    <polygon points="0,676 330,624 366,1040 0,1040" fill="var(--yellow)"/>
    <polygon points="0,1106 380,1106 398,1200 0,1200" fill="var(--ink)"/>
    <polygon points="380,1106 727,1106 727,1200 398,1200" fill="var(--yellow)"/>
    <polygon points="380,1106 391,1106 409,1200 398,1200" fill="var(--paper)"/>
  </svg>

  <div class="brand">
    <span class="brand-mark"></span>
    <span class="brand-name">Dunrock</span>
  </div>

  <section class="intro">
    <h1 class="intro-head">
      <span class="small">With over</span>
      <span class="big">50 Years</span>
      <span class="small">of experience</span>
      <span class="small">in the industry,</span>
    </h1>
    <p class="intro-body">We have what it takes to help<br>you develop your land for your<br>long or short term goals.</p>
  </section>

  <div class="photo photo-lake-dig" role="img" aria-label="Photo of a freshly dug lake bed with trees on the horizon"></div>
  <div class="photo photo-aerial" role="img" aria-label="Aerial photo of cleared brush land with trails"></div>
  <div class="photo photo-pond" role="img" aria-label="Photo of a finished pond with grassy banks"></div>

  <p class="services-farm">We build lakes • ponds •<br>do brush clearing for<br>farmers and ranchers.</p>

  <div class="commercial">
    <span class="commercial-tag">For commercial <em>customers,</em></span>
    <p class="commercial-text">we build building pads •<br>site clearing, pavement<br>and soil stabilization.</p>
  </div>

  <div class="cert-strip">Dunrock Grading Co. HUB/WBE Certified</div>

  <div class="contact-bar">
    <div class="contact contact-web">
      <svg width="28" height="28" viewBox="0 0 24 24" aria-hidden="true">
        <circle cx="12" cy="12" r="11" fill="var(--paper)"/>
        <g fill="none" stroke="var(--ink)" stroke-width="1.4">
          <circle cx="12" cy="12" r="6.5"/>
          <ellipse cx="12" cy="12" rx="3" ry="6.5"/>
          <line x1="5.5" y1="12" x2="18.5" y2="12"/>
        </g>
      </svg>
      <span>DUNROCKGRADERS.COM</span>
    </div>
    <div class="contact contact-phone">
      <svg width="36" height="36" viewBox="0 0 24 24" aria-hidden="true">
        <circle cx="12" cy="12" r="12" fill="var(--ink)"/>
        <path d="M8.6 6.2l1.6 2.6c.2.4.1.8-.2 1.1l-.9.8c.8 1.6 2.1 2.9 3.7 3.7l.8-.9c.3-.3.7-.4 1.1-.2l2.6 1.6c.4.2.5.7.3 1.1l-.9 1.4c-.3.5-.9.7-1.4.6-3.6-.9-6.5-3.8-7.4-7.4-.1-.5.1-1.1.6-1.4l1.4-.9c.4-.2.9-.1 1.1.3z" fill="var(--yellow)"/>
      </svg>
      <span>555.010.2663</span>
    </div>
  </div>
</main>
</body>
</html>
```